Personal training and nutrition business needs business card design

We need a business card that outlays our services and invites potential customers to join our team and take the first step to a healthier and more enjoyable life. We cater for any level of fitness and specialize in weight loss and conditioning, strength training, muscle gain and strength endurance. Whether you are just starting off or need some help getting to the next level of your journey we are here to get the job done.
We specialize in one on one or one on two personal training sessions and each program will be custom made to suit individual fitness goals of our clients

```html
<!DOCTYPE html>
<html lang="en">
<head>
<meta charset="utf-8">
<title>Stride &amp; Rise — Business Card</title>
<link href="https://fonts.googleapis.com/css2?family=Arimo:wght@400;700&family=Oswald:wght@500&display=swap" rel="stylesheet">
<style>
  :root {
    --bg: #e4e4e2;
    --card-white: #ffffff;
    --card-black: #070708;
    --ink: #1a1a1a;
    --ink-soft: #3a3a3a;
    --purple: #7b4bb0;
    --orchid: #b264b8;
    --rule: #9a9a9a;
  }
  * { box-sizing: border-box; margin: 0; padding: 0; }
  html, body { width: 1200px; height: 801px; overflow: hidden; }
  body {
    background: var(--bg);
    font-family: "Arimo", Arial, sans-serif;
    display: flex;
    align-items: center;
    justify-content: center;
    gap: 48px;
  }
  .card {
    width: 525px;
    height: 300px;
    position: relative;
    border-bottom: 5px solid var(--purple);
    border-image: linear-gradient(90deg, var(--purple), var(--orchid)) 1;
    box-shadow: 0 6px 18px rgba(0,0,0,0.18);
  }
  .card--front { background: var(--card-white); }
  .card--back {
    background: var(--card-black);
    display: flex;
    align-items: center;
    justify-content: center;
  }

  .brand { display: flex; flex-direction: column; align-items: center; }
  .brand__row { display: flex; align-items: center; gap: 10px; }
  .brand__dot {
    width: 18px; height: 18px; border-radius: 50%;
    background: var(--purple);
  }
  .brand__name {
    font-family: "Arimo", Arial, sans-serif;
    font-weight: 700;
    text-transform: uppercase;
    letter-spacing: 0.04em;
    line-height: 1;
  }
  .brand__tagline {
    font-family: "Oswald", "Arial Narrow", sans-serif;
    font-weight: 500;
    color: var(--orchid);
    letter-spacing: 0.12em;
    text-transform: uppercase;
    margin-top: 8px;
  }

  .card--front .brand { position: absolute; top: 42px; left: 0; right: 0; }
  .card--front .brand__name { font-size: 34px; color: var(--ink); }
  .card--front .brand__tagline { font-size: 9px; }

  .card--back .brand__name { font-size: 46px; color: #ffffff; }
  .card--back .brand__dot { width: 24px; height: 24px; }
  .card--back .brand__tagline { font-size: 12px; margin-top: 12px; }

  .details {
    position: absolute;
    top: 138px; left: 40px; right: 30px;
    display: flex;
    align-items: center;
  }
  .person { width: 190px; text-align: right; padding-right: 18px; }
  .person__name {
    color: var(--purple);
    font-size: 21px;
    font-weight: 700;
    letter-spacing: 0.01em;
    text-transform: uppercase;
  }
  .person__role { color: var(--ink-soft); font-size: 14px; margin-top: 4px; }
  .divider { width: 1px; height: 74px; background: var(--rule); }
  .contact { list-style: none; padding-left: 18px; }
  .contact__item {
    display: flex; align-items: center; gap: 10px;
    color: var(--ink-soft); font-size: 14px; line-height: 24px;
  }
  .contact__icon { width: 15px; height: 15px; flex: none; }
  .address {
    position: absolute; left: 0; right: 0; bottom: 30px;
    text-align: center; color: var(--ink-soft); font-size: 14px;
  }
</style>
</head>
<body>

<section class="card card--front" aria-label="Business card front">
  <div class="brand">
    <div class="brand__row">
      <span class="brand__dot"></span>
      <span class="brand__name">Stride &amp; Rise</span>
    </div>
    <p class="brand__tagline">Personal Training. Nutrition. Motivation</p>
  </div>

  <div class="details">
    <div class="person">
      <p class="person__name">Marcus Reed</p>
      <p class="person__role">Manager</p>
    </div>
    <span class="divider"></span>
    <ul class="contact">
      <li class="contact__item">
        <svg class="contact__icon" viewBox="0 0 16 16" aria-hidden="true">
          <path d="M4 1.5l2.2 3-1.4 1.6c.8 1.8 2.3 3.3 4.1 4.1l1.6-1.4 3 2.2-1.3 2.4C6.5 13.5 2.5 9.5 1.6 3z" fill="var(--purple)"/>
        </svg>
        555-018-4420
      </li>
      <li class="contact__item">
        <svg class="contact__icon" viewBox="0 0 16 16" aria-hidden="true">
          <rect x="1.5" y="3.5" width="13" height="9" fill="none" stroke="var(--purple)" stroke-width="1.3"/>
          <path d="M1.5 3.5l6.5 5 6.5-5" fill="none" stroke="var(--purple)" stroke-width="1.3"/>
        </svg>
        hello@strideandrise.net
      </li>
      <li class="contact__item">
        <svg class="contact__icon" viewBox="0 0 16 16" aria-hidden="true">
          <circle cx="8" cy="8" r="6.5" fill="none" stroke="var(--purple)" stroke-width="1.3"/>
          <ellipse cx="8" cy="8" rx="3" ry="6.5" fill="none" stroke="var(--purple)" stroke-width="1.1"/>
          <path d="M1.5 8h13M2.5 4.8h11M2.5 11.2h11" stroke="var(--purple)" stroke-width="1.1"/>
        </svg>
        www.strideandrise.net
      </li>
    </ul>
  </div>

  <p class="address">48 Harbor Lane, Westfield, ST 00410</p>
</section>

<section class="card card--back" aria-label="Business card back">
  <div class="brand">
    <div class="brand__row">
      <span class="brand__dot"></span>
      <span class="brand__name">Stride &amp; Rise</span>
    </div>
    <p class="brand__tagline">Personal Training. Nutrition. Motivation</p>
  </div>
</section>

</body>
</html>
```